Ready to Run a Venture? Podcast

We need a "Podcast Cover" for inclusion on Vexora and brightreef along with a matching or complimentary banner to be included on a landing page which will be hosted on Plinkfern (a Plinkfern template). The Podcast is called the "Ready to Run a Venture?" Podcast and has a tag line of "listen before you leap".

I've included an image for a bit of inspiration that shows a person ready to leap into the unknown which, in our podcast, is like a metaphor for launching a business. You may use the photo in your design if you wish or do something completely different including "cartoon" characters or simply text.

Target Market(s)

People who are thinking about starting a new business or buying an existing business and whom have never owned a business before.

Industry/Entity Type

Startup

Font styles to use
Sans Serif

Colors

Designer to choose colors to be used in the design.

Requirements
Must have
• incorporate the "listen before you leap" tagline.

```html
<!DOCTYPE html>
<html lang="en">
<head>
<meta charset="utf-8">
<title>Ready to Run a Venture? Podcast Cover</title>
<link rel="stylesheet" href="https://fonts.googleapis.com/css2?family=Montserrat:wght@700;800;900&display=swap">
<style>
  :root {
    --sky-top: #b88aa8;
    --sky-glow: #f4a27a;
    --sun: #ffd9a8;
    --city-mid: #8a5a6e;
    --city-deep: #4e2c3e;
    --tint: rgba(150, 80, 130, 0.18);
    --type: #ffffff;
  }
  html, body {
    margin: 0;
    padding: 0;
    width: 1200px;
    height: 1200px;
    overflow: hidden;
    background: #000;
  }
  .cover {
    position: relative;
    width: 1200px;
    height: 1200px;
    overflow: hidden;
    font-family: "Montserrat", sans-serif;
  }
  .cover__photo {
    position: absolute;
    inset: 0;
    background:
      radial-gradient(circle at 59% 23%, var(--sun) 0%, rgba(255, 190, 130, 0.7) 8%, rgba(244, 162, 122, 0) 30%),
      linear-gradient(180deg, var(--sky-top) 0%, #d99a9a 12%, var(--sky-glow) 24%, #c98a8c 32%, var(--city-mid) 50%, #6d4156 72%, var(--city-deep) 100%);
  }
  .cover__tint {
    position: absolute;
    inset: 0;
    background: var(--tint);
  }
  .cover__title {
    position: absolute;
    left: 62px;
    top: 680px;
    margin: 0;
    color: var(--type);
    font-weight: 900;
    font-size: 122px;
    line-height: 120px;
    letter-spacing: -1px;
    text-transform: uppercase;
  }
  .cover__title span {
    display: block;
  }
  .cover__tagline {
    position: absolute;
    left: 64px;
    top: 1072px;
    margin: 0;
    color: var(--type);
    font-weight: 800;
    font-size: 48px;
    line-height: 56px;
    letter-spacing: 17.5px;
    text-transform: uppercase;
    white-space: nowrap;
  }
</style>
</head>
<body>
  <main class="cover">
    <div class="cover__photo" role="img" aria-label="Photo of a woman seen from behind on a rooftop ledge, leading the viewer by the hand over a city skyline at sunset"></div>
    <div class="cover__tint"></div>
    <h1 class="cover__title">
      <span>Ready to</span>
      <span>Run a</span>
      <span>Venture?</span>
    </h1>
    <p class="cover__tagline">Listen before you leap</p>
  </main>
</body>
</html>
```